Voltline Assemblies, Inc. Business Card

Voltline has three operating entities and I'm looking for a standard business card template that can be used for Voltline and the three operating entities that the logo just get swapped out, but has a very similar look and feel. Ultimately if someone had a business card from each, they assume the organizations are related because they all have the same look and feel.
Below are our websites and I will attached the logos for each entity:
https://www.voltlineassemblies.example/
https://www.brantoceramic.example/
https://www.omra-kfsd.example/
https://www.summitbreaker.example/

Target Market(s)

US Voltline

Industry/Entity Type

US Voltline

Contact Information for Business Card

Normal stuff

```html
<!DOCTYPE html>
<html lang="en">
<head>
<meta charset="utf-8">
<title>Voltline Assemblies, Inc. Business Card</title>
<link rel="stylesheet" href="https://fonts.googleapis.com/css2?family=Open+Sans:wght@400;600;700&display=swap">
<style>
  :root {
    --navy: #223068;
    --navy-soft: #2e3d7a;
    --red: #c32033;
    --white: #ffffff;
    --stage: #e6e7ea;
  }
  * { box-sizing: border-box; margin: 0; padding: 0; }
  html, body {
    width: 1200px; height: 1015px; overflow: hidden;
    background: var(--stage);
    font-family: "Open Sans", Arial, sans-serif;
  }
  .sheet {
    width: 1200px; height: 1015px;
    display: flex; flex-direction: column; align-items: center; justify-content: center;
    gap: 34px;
  }
  .card {
    position: relative;
    width: 820px; height: 469px;
    background: var(--navy);
    overflow: hidden;
    box-shadow: 0 6px 18px rgba(0,0,0,0.18);
  }
  .card__band {
    position: absolute; left: 0; right: 0; bottom: 0;
    height: 16px; background: var(--red);
  }
  /* Front */
  .brand {
    position: absolute; left: 50%; top: 46%;
    transform: translate(-50%, -50%);
    display: flex; align-items: center; gap: 22px;
  }
  .brand__dot {
    width: 88px; height: 88px; border-radius: 50%;
    background: var(--red); flex: none;
  }
  .brand__name {
    color: var(--white); font-weight: 700;
    font-size: 44px; line-height: 1.05; letter-spacing: 0.5px;
    text-transform: uppercase;
  }
  .brand__name span { display: block; font-size: 22px; letter-spacing: 4px; }
  /* Back */
  .emblem-area {
    position: absolute; right: 30px; top: 36px;
    width: 360px; height: 360px; border-radius: 50%;
    background: radial-gradient(circle at 45% 40%, #3c4b88, var(--navy-soft));
  }
  .contact {
    position: absolute; left: 64px; top: 150px;
    width: 350px;
    color: var(--white);
  }
  .contact__name {
    color: var(--red); font-weight: 600; font-size: 26px;
    text-transform: uppercase; line-height: 1.1;
  }
  .contact__role {
    font-size: 16px; text-transform: uppercase; letter-spacing: 0.3px;
  }
  .contact__list { list-style: none; margin-top: 34px; }
  .contact__list li {
    display: flex; align-items: center; gap: 12px;
    font-size: 19px; line-height: 1.5; white-space: nowrap;
  }
  .contact__list svg { width: 18px; height: 18px; flex: none; }
  .contact__address {
    margin-top: 34px; font-size: 19px; line-height: 1.35;
    font-style: normal; white-space: nowrap;
  }
</style>
</head>
<body>
<main class="sheet">
  <section class="card card--front" aria-label="Card front">
    <div class="brand">
      <div class="brand__dot"></div>
      <div class="brand__name">Voltline<span>Assemblies, Inc.</span></div>
    </div>
    <div class="card__band"></div>
  </section>

  <section class="card card--back" aria-label="Card back">
    <div class="emblem-area" role="img" aria-label="Large brand emblem artwork"></div>
    <div class="contact">
      <h1 class="contact__name">Marcus Hale</h1>
      <p class="contact__role">Managing Director</p>
      <ul class="contact__list">
        <li>
          <svg viewBox="0 0 24 24" aria-hidden="true"><path fill="#c32033" d="M6.6 10.8a15.2 15.2 0 0 0 6.6 6.6l2.2-2.2a1 1 0 0 1 1-.25 11.4 11.4 0 0 0 3.6.57 1 1 0 0 1 1 1V20a1 1 0 0 1-1 1A17 17 0 0 1 3 4a1 1 0 0 1 1-1h3.5a1 1 0 0 1 1 1c0 1.25.2 2.45.57 3.57a1 1 0 0 1-.25 1z"/></svg>
          044-987 654 321
        </li>
        <li>
          <svg viewBox="0 0 24 24" aria-hidden="true"><rect x="2" y="5" width="20" height="14" fill="#c32033"/><path d="M2 5l10 8 10-8" fill="none" stroke="#223068" stroke-width="1.8"/></svg>
          info@voltline.example
        </li>
        <li>
          <svg viewBox="0 0 24 24" aria-hidden="true"><g fill="none" stroke="#c32033" stroke-width="2"><circle cx="12" cy="12" r="9"/><ellipse cx="12" cy="12" rx="4" ry="9"/><path d="M3 12h18M5 7h14M5 17h14"/></g></svg>
          www.voltline.example
        </li>
      </ul>
      <address class="contact__address">1280 Foundry Road, Suite 4<br>Dayton, OH 45402</address>
    </div>
    <div class="card__band"></div>
  </section>
</main>
</body>
</html>
```